Lorvika.no is a new website about pedagogical entrepreneurship. It's main target group is teachers. The Fjellmark Institute for Classroom Media and the Nordvik Agency for Schools and Study are leading the project.

The web page is meant to show examples of how different methods of entrepreneurship can be used pedagogical in a learning environment. The page will also support the user with examples of different teaching programs and other examples of best practice.

Pedagogical entrepreneurship is not about business and men in suits. It's a method for learning. The focus in the design should be on school, education and new ways of learning.

The final product should be motivating and engaging, but at the same time governmental and serious. We are not looking for something "flashy" and corporate-looking, but a moderate, task-focused and clean design that state quality.

We need designs for three pages:
1 - frontpage
2 - subpage ("Metoder og undervisningsopplegg")
3 - subpage ("Smått-VERK i Brekkelia")

The interaction design for these three pages will be uploaded as an attachment.

We would like you to find inspiration in the following websites:
- www.gryvekst.no
- www.lavrek.no
- www.tovandstudio.com
- www.kvp.no
(more will be added)

Please use the attached logo, and feel free to use this as an inspiration for the rest of the design.

Target Market(s)

Teachers

Industry/Entity Type

Education

Requirements
Must have
• * Header with: Logo. Main navigation. Utility navigation. Search box.
* Footer
Should not have
• Images of men in suits.
Very strong graphical elements that stands out too much (we want it clean).

```html
<!DOCTYPE html>
<html lang="en">
<head>
<meta charset="utf-8">
<title>Lorvika.no – Pedagogical Entrepreneurship</title>
<link rel="stylesheet" href="https://fonts.googleapis.com/css2?family=Didact+Gothic&family=Arimo:wght@400;700&display=swap">
<style>
:root{
  --navy:#1f4677;
  --navy-dark:#173a66;
  --navy-mid:#24528a;
  --sky:#1e8fd0;
  --sky-light:#4cb2e6;
  --title-blue:#1a86c8;
  --text:#222;
  --muted:#555;
  --white:#fff;
  --nav-grey:#ececec;
}
*{box-sizing:border-box;margin:0;padding:0}
html,body{width:950px;height:1200px;overflow:hidden}
body{position:relative;background:var(--navy);font-family:Arimo,Arial,sans-serif;color:var(--text)}
a{color:inherit}
.abs{position:absolute}
.display{font-family:"Didact Gothic",sans-serif}

/* header */
.site-header{left:0;top:0;width:950px;height:104px;background:linear-gradient(#1b426f,#24508a)}
.brand{left:90px;top:18px;display:flex;align-items:center;gap:12px}
.brand-mark{width:54px;height:54px;border-radius:50%;background:var(--sky-light)}
.brand-name{font-family:"Didact Gothic",sans-serif;font-size:44px;color:var(--sky-light);line-height:1}
.brand-tagline{left:175px;top:68px;font-size:9px;color:#cfe0f2}
.call{left:640px;top:22px;width:222px;text-align:right;color:var(--white);font-family:"Didact Gothic",sans-serif}
.call .lead{font-size:12.5px}
.call .num{font-size:19px;line-height:1.1}
.utility{left:528px;top:81px;display:flex;gap:26px;font-size:10px;color:var(--white)}
.social{left:768px;top:76px;display:flex;gap:5px}
.social span{width:21px;height:20px;border-radius:2px;background:#2f7fc4;display:block}
.social span:first-child{background:#c6272b}

/* nav */
.main-nav{left:0;top:104px;width:950px;height:40px;background:linear-gradient(#fafafa,#e2e2e2)}
.tabs{left:87px;top:104px;display:flex;height:40px}
.tabs a{width:180px;display:flex;align-items:center;justify-content:center;font-family:"Didact Gothic",sans-serif;font-size:12px;color:#2a3c55;text-decoration:none;border-right:1px solid #d0d0d0}
.tabs a.active{background:linear-gradient(#4fb0e4,#1d86c8);color:var(--white);border:0}
.search{left:687px;top:112px;width:146px;height:24px;border:1px solid #ccc;background:var(--white);font-size:8px;color:#aaa;padding:7px 10px;font-style:italic}
.search-btn{left:834px;top:112px;width:28px;height:24px;background:var(--sky);border-radius:0 2px 2px 0}
.nav-rule{left:0;top:144px;width:950px;height:8px;background:var(--navy-mid)}

.hero{left:0;top:152px;width:950px;height:298px;background:linear-gradient(100deg,#a9aeac 0%,#c4c8c5 45%,#9aa2a8 75%,#6a6e72 100%)}

/* content */
.content{left:87px;top:454px;width:775px;height:572px;background:var(--white)}
.feature{top:462px;width:228px;height:70px;background:linear-gradient(#3c6fb0,#1c4a85);border:1px solid #6e92c0;box-shadow:2px 2px 4px rgba(0,0,0,.3);color:var(--white);display:flex;align-items:center;gap:8px;padding-left:8px}
.feature .icon{width:56px;height:40px;flex:none;border-radius:3px}
.feature h3{font-family:"Didact Gothic",sans-serif;font-weight:400;font-size:16px;line-height:16px;letter-spacing:.3px}
.feature em{font-size:9px;display:block;margin-top:2px}

.meter-panel{left:103px;top:549px;width:236px;height:261px;background:linear-gradient(#2d63a4,#1e4a85);border:1px solid #5d86bb;box-shadow:2px 2px 4px rgba(0,0,0,.3)}
.meter-head{height:41px;background:linear-gradient(#5ebdf0,#1e8fd0);color:var(--white);font-family:"Didact Gothic",sans-serif;font-size:15px;line-height:16px;padding:5px 10px}
.meter-graphic{position:absolute;left:12px;top:52px;width:210px;height:160px;border-radius:6px;background:radial-gradient(circle at 55% 50%,#5c86b8,#2a5a97 70%)}
.meter-link{position:absolute;left:0;right:0;bottom:11px;text-align:center;color:var(--white);font-family:"Didact Gothic",sans-serif;font-size:13px;text-decoration:underline}

.welcome{left:356px;top:548px;width:490px}
.welcome h1{font-family:"Didact Gothic",sans-serif;font-weight:400;color:var(--title-blue);font-size:16.5px;margin-bottom:6px}
.welcome p{font-size:8.7px;line-height:11.5px;margin-bottom:11px}

.get-started{left:354px;top:664px;width:492px;height:146px;background:linear-gradient(#2d63a4,#1e4a85);border:1px solid #5d86bb;box-shadow:2px 2px 4px rgba(0,0,0,.3);color:var(--white);padding:5px 10px}
.get-started h2{font-size:15px;font-weight:700;margin-bottom:5px}
.gs-col{position:absolute;top:28px}
.gs-col h4{font-family:"Didact Gothic",sans-serif;font-weight:400;font-size:12.5px;margin-bottom:2px}
.gs-col a{display:block;font-size:8.6px;line-height:14.8px;text-decoration:underline}
.btn{display:inline-block;margin-top:4px;background:#f3f3f3;color:#333;font-size:7px;padding:2px 5px;border-radius:2px}

.inspiration{left:103px;top:826px;width:743px;height:36px;background:linear-gradient(#56b7ec,#1e8fd0);color:var(--white);font-family:"Didact Gothic",sans-serif;font-size:18px;padding:6px 14px}
.arrow{top:910px;width:40px;height:40px}
.slide{top:874px;width:212px;height:110px;border-radius:3px}
.caption{top:990px;width:212px;text-align:center;font-family:"Didact Gothic",sans-serif;font-size:12.5px;color:#333}

/* footer */
.site-footer{left:0;top:1027px;width:950px;height:137px;background:var(--white)}
.footer-mark{left:104px;top:1058px;width:78px;height:78px;border-radius:50%;background:linear-gradient(#4cb2e6,#1f4677)}
.fcol{top:1040px}
.fcol h5{font-family:"Didact Gothic",sans-serif;font-weight:400;color:var(--title-blue);font-size:15px;line-height:13.5px;margin-bottom:4px}
.fcol ul{list-style:none;font-size:8.8px}
.fcol li{line-height:14.8px;padding-left:8px;position:relative}
.fcol li::before{content:"";position:absolute;left:0;top:6px;width:3px;height:3px;border-radius:50%;background:#222}
.fcol li a{text-decoration:underline}
.fcol li.more{font-weight:700;font-size:9.5px}
.fcol li.plain::before{display:none}
.bottom-bar{left:0;top:1164px;width:950px;height:36px;background:var(--navy);color:var(--white);font-size:8px}
.bottom-bar .links{position:absolute;left:102px;top:14px}
.bottom-bar .copy{position:absolute;right:101px;top:14px}
</style>
</head>
<body>

<header class="site-header abs"></header>
<div class="brand abs"><span class="brand-mark"></span><span class="brand-name">Lorvika</span></div>
<div class="brand-tagline abs">Entreprenørielle metoder i undervisningen</div>
<div class="call abs"><div class="lead">Call Now to Find Out More:</div><div class="num">555 - 014 - 220 -91</div></div>
<nav class="utility abs"><a href="#">New User?</a><a href="#">Register</a><a href="#">Sign in</a><a href="#">Help</a></nav>
<div class="social abs" aria-label="Social links"><span></span><span></span><span></span><span></span></div>

<div class="main-nav abs"></div>
<nav class="tabs abs">
  <a class="active" href="#">Best Practice schools</a>
  <a href="#">Lorvikameter</a>
  <a href="#">About Lorvika.no</a>
</nav>
<div class="search abs">Search...</div>
<div class="search-btn abs">
  <svg width="28" height="24" viewBox="0 0 28 24"><circle cx="13" cy="11" r="4.5" fill="none" stroke="#fff" stroke-width="1.8"/><line x1="16.2" y1="14.2" x2="19.5" y2="17.5" stroke="#fff" stroke-width="2.2"/></svg>
</div>
<div class="nav-rule abs"></div>

<div class="hero abs" role="img" aria-label="Photo of a teacher at a chalkboard covered in chemistry formulas, with pupils raising hands"></div>

<main class="content abs"></main>

<div class="feature abs" style="left:103px">
  <div class="icon" role="img" aria-label="Open book illustration" style="background:linear-gradient(#e8eef5,#9fb3c9)"></div>
  <div><h3>What is Pedagogical Entrepreneurship</h3><em>Learn About what, why and how !</em></div>
</div>
<div class="feature abs" style="left:362px">
  <div class="icon" role="img" aria-label="Calendar illustration" style="width:46px;background:linear-gradient(#fff,#d8dee6)"></div>
  <div><h3>Methods and Teaching Plans</h3><em>Plan Your Lessons !</em></div>
</div>
<div class="feature abs" style="left:619px">
  <div class="icon" role="img" aria-label="Light bulb illustration" style="width:40px;background:radial-gradient(circle at 50% 40%,#ffd54a,#f0a800 60%,transparent 62%)"></div>
  <div><h3>Good Examples / Best Practice</h3><em>Be Inspired !</em></div>
</div>

<section class="meter-panel abs">
  <div class="meter-head">Are you working entrepreneurship - like</div>
  <div class="meter-graphic" role="img" aria-label="White gauge dial illustration with a needle"></div>
  <a class="meter-link" href="#">Try the Lorvikameter !</a>
</section>

<section class="welcome abs">
  <h1>Welcome to Pedagogical Entrepreneurship</h1>
  <p>Lorem Ipsum is simply dummy text of the printing and typesetting industry. Lorem Ipsum has been the industry's standard dummy text ever since the 1500s, when an unknown printer took a galley of type and scrambled it to make a type specimen book.</p>
  <p>It has survived not only five centuries, but also the leap into electronic typesetting, remaining essentially unchanged. It was popularised in the 1960s with the release of Kervane sheets containing Lorem Ipsum passages.and more recently with desktop publishing software like Quillset Layout including versions of Lorem Ipsum.</p>
</section>

<section class="get-started abs">
  <h2>Get Started</h2>
  <div class="gs-col" style="left:10px"><h4>Methods</h4><a href="#">Lorem Ipsum</a><a href="#">typesetting industry</a><a href="#">Scrambled</a><a href="#">Electronic typesetting</a><a href="#">Kervane sheets</a><span class="btn">See More</span></div>
  <div class="gs-col" style="left:189px"><h4>Teaching Plans</h4><a href="#">Lorem Ipsum</a><a href="#">typesetting industry</a><a href="#">Scrambled</a><a href="#">Electronic typesetting</a><a href="#">Kervane sheets</a><span class="btn">See More</span></div>
  <div class="gs-col" style="left:388px"><h4>Services</h4><a href="#">Lorem Ipsum</a><a href="#">typesetting industry</a><a href="#">Scrambled</a><a href="#">Electronic typesetting</a><a href="#">Kervane sheets</a><span class="btn">See More</span></div>
</section>

<div class="inspiration abs">Inspiration</div>
<svg class="arrow abs" style="left:102px" viewBox="0 0 40 40"><circle cx="20" cy="20" r="19" fill="#1e8fd0" stroke="#e6eef6" stroke-width="2"/><path d="M25 11 L12 20 L25 29 Z" fill="#fff"/></svg>
<div class="slide abs" style="left:150px;background:linear-gradient(#a8bfd8 0%,#b98a6c 45%,#7b6f66 100%)" role="img" aria-label="Photo of a brick school building"></div>
<div class="slide abs" style="left:369px;background:linear-gradient(#9cc0e0 0%,#a87c64 40%,#6f9a55 100%)" role="img" aria-label="Photo of a school building with green lawn"></div>
<div class="slide abs" style="left:587px;background:linear-gradient(#c8dce8 0%,#d9d3c8 45%,#8ca06e 100%)" role="img" aria-label="Photo of a school courtyard"></div>
<svg class="arrow abs" style="left:808px" viewBox="0 0 40 40"><circle cx="20" cy="20" r="19" fill="#1e8fd0" stroke="#e6eef6" stroke-width="2"/><path d="M15 11 L28 20 L15 29 Z" fill="#fff"/></svg>
<div class="caption abs" style="left:150px">Smått-VERK at Brekkelia School</div>
<div class="caption abs" style="left:369px">Smått-VERK at Brekkelia School</div>
<div class="caption abs" style="left:587px">Smått-VERK at Brekkelia School</div>

<footer class="site-footer abs"></footer>
<div class="footer-mark abs"></div>
<div class="fcol abs" style="left:202px"><h5>Pedagogical<br>Entrepreneurship</h5><ul><li><a href="#">What is pedagogical<br>entrepreneurship</a></li><li><a href="#">Science</a></li><li><a href="#">Best Practice Schools</a></li><li><a href="#">Lorvikameteret</a></li><li><a href="#">About Lorvika.no</a></li></ul></div>
<div class="fcol abs" style="left:394px;top:1050px"><h5>Methods</h5><ul><li><a href="#">Story line</a></li><li><a href="#">Real</a></li><li><a href="#">Cafe Pedagogical</a></li><li class="more plain"><a href="#">See More</a></li></ul></div>
<div class="fcol abs" style="left:552px;top:1050px"><h5>Gode eksempler</h5><ul><li><a href="#">Lorem Ipsum</a></li><li><a href="#">typesetting industry</a></li><li><a href="#">Scrambled</a></li><li><a href="#">Electronic typesetting</a></li><li class="more"><a href="#">See More</a></li></ul></div>
<div class="fcol abs" style="left:735px;top:1050px"><h5>Teaching Plans</h5><ul><li><a href="#">Lorem Ipsum</a></li><li><a href="#">typesetting industry</a></li><li><a href="#">Scrambled</a></li><li><a href="#">Electronic typesetting</a></li><li class="more"><a href="#">See More</a></li></ul></div>

<div class="bottom-bar abs">
  <div class="links">Best Practice schools &nbsp;|&nbsp; Lorvikameter &nbsp;|&nbsp; About Lorvika.no</div>
  <div class="copy">© Copyrights 2012 All rights Reserved</div>
</div>

</body>
</html>
```